exciting cleaing project

I need a cleaning website built. It has to be built for a woman. the domain name is gwenshines.net.

I need the designer to find the images and code the site. the site needs to be about five pages.

here are some good examples:

https://www.tidypetal.com/gainesville/

http://abrightwren.com/

https://brisknookgainesville.com/services/

https://www.hevo.com/housekeepers/gainesville-fl

https://glintrow.com/

Target Market(s)

home cleaning,

Industry/Entity Type

Cleaning Service

Coding

Coded - Design and coding required

Number of Pages Required

4 page

Font styles to use
Script

Colors
33a6d7
85acd3
f04a50
ec1f27

Requirements
Must have
• nice design
Nice to have
• residential
Should not have
• commercial

```html
<!DOCTYPE html>
<html lang="en">
<head>
<meta charset="utf-8">
<title>Gwen Shines — Home Cleaning</title>
<link href="https://fonts.googleapis.com/css2?family=Lato:wght@400;700;900&family=Satisfy&display=swap" rel="stylesheet">
<style>
:root{
  --blue:#33a6d7;
  --soft-blue:#85acd3;
  --red:#ec1f27;
  --coral:#f04a50;
  --ink:#222;
  --grey-bg:#f0f0f0;
  --footer:#1e2b37;
  --white:#fff;
}
*{box-sizing:border-box;margin:0;padding:0}
html,body{width:1200px;height:3560px;overflow:hidden}
body{font-family:"Lato",sans-serif;color:var(--ink);background:var(--white);position:relative}
.script{font-family:"Satisfy",cursive;font-weight:400}
section,header,footer{position:absolute;left:0;width:1200px}
.abs{position:absolute}

/* header */
.site-header{top:0;height:70px;background:var(--white)}
.brand{left:113px;top:12px;font-size:32px;font-weight:900;color:var(--red)}
.main-nav{left:543px;top:26px;font-size:14px;display:flex;gap:0}
.main-nav a{position:absolute;color:#333;text-decoration:none;white-space:nowrap}
.header-call{left:925px;top:8px;width:163px;text-align:center}
.header-call .label{font-size:12px;font-weight:900;color:#111;letter-spacing:.3px}
.header-call .phone{margin-top:4px;height:32px;background:var(--red);color:var(--white);font-size:19px;font-weight:900;line-height:32px;letter-spacing:.5px}

/* hero */
.hero{top:70px;height:567px;background:linear-gradient(90deg,#3a2a22 0%,#6b4a36 35%,#8a6a52 60%,#c9b6a4 85%,#e3d8cc 100%)}
.hero-title{left:124px;top:82px;width:490px;text-align:center;color:var(--white);font-size:35px;font-weight:900;line-height:38px}
.booking{left:124px;top:176px;width:490px;height:346px;background:rgba(0,0,0,.72)}
.booking h2{position:absolute;left:0;top:14px;width:100%;text-align:center;color:var(--white);font-size:38px}
.field{position:absolute;border:1px solid #ddd;color:#ddd;font-size:11px;padding:7px 13px}
.captcha{position:absolute;left:104px;top:274px;width:162px;height:39px;background:#f6f6f6;border-radius:2px}
.captcha .box{position:absolute;left:9px;top:12px;width:14px;height:14px;border:2px solid #c1c1c1;background:#fff}
.captcha .txt{position:absolute;left:30px;top:13px;font-size:8px;color:#333}
.captcha .badge{position:absolute;right:10px;top:8px;width:20px;height:20px;border-radius:50%;background:#9fb6d8}
.send-btn{position:absolute;left:274px;top:275px;width:112px;height:36px;background:var(--red);color:var(--white);font-weight:700;font-size:17px;text-align:center;line-height:36px}

/* provide */
.provide{top:637px;height:217px;background:var(--grey-bg)}
.provide h2{position:absolute;top:48px;width:100%;text-align:center;font-size:42px;color:#111}
.pill{position:absolute;top:119px;height:39px;border-radius:20px;background:var(--blue);color:var(--white);font-weight:900;font-size:15px;line-height:39px;text-align:center;letter-spacing:.3px}

/* cleaning types */
.types{top:854px;height:812px;background:linear-gradient(90deg,#f4f1ee 0%,#f1ede9 38%,#dfe3e2 60%,#c7cfcc 80%,#b6c3bf 100%)}
.types h2{position:absolute;left:113px;top:52px;font-size:40px;color:#111}
.type{position:absolute;width:170px;text-align:center}
.type .photo{position:absolute;left:31px;top:0;width:108px;height:108px;border-radius:50%;border:2px solid var(--coral)}
.type .icon{position:absolute;left:53px;top:88px;width:64px;height:64px;border-radius:50%;background:var(--coral);display:flex;align-items:center;justify-content:center}
.type .name{position:absolute;top:158px;width:100%;font-size:16px;font-weight:700}
.pledge{left:113px;top:598px;width:972px;height:156px;background:#f7f4f2;border:4px solid #fff;box-shadow:0 1px 4px rgba(0,0,0,.12);text-align:center;font-size:21px;line-height:28px;padding-top:32px;color:#222}

/* services */
.services{top:1666px;height:549px;background:linear-gradient(90deg,#e2d9d4,#ebe3df 50%,#e6dcd7)}
.card{position:absolute;top:66px;width:329px;height:418px}
.card .photo{height:217px}
.card .body{height:201px;background:var(--blue);color:var(--white);padding:24px 20px}
.card h3{font-size:18px;font-weight:700;letter-spacing:.3px}
.card h4{font-size:14px;font-weight:700;margin-top:9px}
.card p{font-size:11px;line-height:19.5px;margin-top:6px}

/* intro */
.intro{top:2215px;height:232px;text-align:center}
.intro .kicker{position:absolute;top:48px;width:100%;font-size:32px;color:var(--red)}
.intro h2{position:absolute;top:94px;width:100%;font-size:28px;font-weight:900;letter-spacing:.5px;color:#111}
.intro .tag{position:absolute;left:513px;top:153px;width:174px;height:36px;background:var(--red);color:var(--white);font-weight:700;font-size:15px;line-height:36px}
.rule{position:absolute;height:1px}

/* about */
.about{top:2447px;height:521px}
.about h2{position:absolute;left:113px;top:128px;font-size:40px;color:#111}
.about h3{position:absolute;left:113px;top:176px;font-size:26px;font-weight:700;color:var(--blue)}
.about p{position:absolute;left:113px;top:226px;width:396px;font-size:13px;line-height:23.5px;color:#444}
.about .photo{left:558px;top:59px;width:530px;height:390px;background:linear-gradient(135deg,#8a9a72,#c8c0ad 40%,#7a5a44 70%,#5a3e2e)}

/* footer */
.site-footer{top:3097px;height:421px;background:var(--footer);color:#d0d6dc}
.cta{left:112px;top:2968px;width:976px;height:170px;background:var(--blue);text-align:center;color:var(--white)}
.cta .name{position:absolute;top:22px;width:100%;font-size:50px}
.cta .call{position:absolute;top:82px;width:100%;font-size:48px;font-weight:900;text-decoration:underline;text-underline-offset:6px;text-decoration-thickness:3px}
.col{position:absolute;top:116px}
.col h5{font-size:20px;font-weight:700;color:var(--white)}
.col ul{list-style:none;margin-top:26px}
.col li{font-size:12px;height:34.5px;padding-left:15px;position:relative}
.col li::before{content:"";position:absolute;left:0;top:5px;width:5px;height:5px;border-radius:50%;background:var(--red)}
.hours{margin-top:26px;font-size:12px;line-height:19px}
.contact-line{display:flex;align-items:center;gap:12px;font-size:12px;margin-top:26px}
.social{display:flex;gap:8px;margin-top:38px}
.social span{width:36px;height:36px;border-radius:50%;background:var(--red)}
.copyright{top:3518px;height:42px;background:var(--blue);color:var(--white);font-size:11px;text-align:center;line-height:42px}
</style>
</head>
<body>

<header class="site-header">
  <div class="abs brand">Gwen Shines</div>
  <nav class="abs main-nav">
    <a style="left:0">Home</a>
    <a style="left:80px">About</a>
    <a style="left:162px">Services</a>
    <a style="left:257px">Contact</a>
  </nav>
  <div class="abs header-call">
    <div class="label">GWEN SHINES</div>
    <div class="phone">352-555-0148</div>
  </div>
</header>

<section class="hero" role="img" aria-label="Photo of a smiling cleaner in yellow gloves wiping an oven in a wooden kitchen">
  <h1 class="abs hero-title">Our Mission at<br>Gwen's Shine is simple</h1>
  <form class="abs booking">
    <h2 class="script">Booking Now</h2>
    <div class="field" style="left:32px;top:76px;width:210px;height:32px">Name:</div>
    <div class="field" style="left:248px;top:76px;width:210px;height:32px">Email:</div>
    <div class="field" style="left:32px;top:118px;width:210px;height:32px">Subject:</div>
    <div class="field" style="left:248px;top:118px;width:210px;height:32px">Phone:</div>
    <div class="field" style="left:32px;top:159px;width:426px;height:32px">Address:</div>
    <div class="field" style="left:32px;top:201px;width:426px;height:60px">Message:</div>
    <div class="captcha"><span class="box"></span><span class="txt">I'm not a robot</span><span class="badge"></span></div>
    <div class="send-btn">Send Now</div>
  </form>
</section>

<section class="provide">
  <h2 class="script">What We Provide</h2>
  <div class="pill" style="left:260px;width:124px">WEEKLY</div>
  <div class="pill" style="left:398px;width:125px">BI-WEEKLY</div>
  <div class="pill" style="left:535px;width:125px">MONTHLY</div>
  <div class="pill" style="left:672px;width:268px">CUSTOM CLEANS AVAILABLE</div>
</section>

<section class="types">
  <div class="abs" role="img" aria-label="Photo of two cleaners in green overalls wiping and mopping a bright white kitchen" style="left:440px;top:0;width:760px;height:600px;background:linear-gradient(90deg,rgba(255,255,255,0),rgba(190,205,200,.35))"></div>
  <h2 class="script">Cleaning Types</h2>

  <div class="type" style="left:102px;top:123px">
    <div class="photo" role="img" aria-label="Bedroom interior photo" style="background:linear-gradient(135deg,#8a6a5a,#c9b2a0)"></div>
    <div class="icon"><svg width="30" height="22" viewBox="0 0 30 22" fill="#fff"><rect x="2" y="2" width="26" height="8" rx="2"/><rect x="0" y="10" width="30" height="8"/><rect x="1" y="18" width="3" height="4"/><rect x="26" y="18" width="3" height="4"/></svg></div>
    <div class="name">Bedroom Interior</div>
  </div>
  <div class="type" style="left:268px;top:123px">
    <div class="photo" role="img" aria-label="Bathroom interior photo" style="background:linear-gradient(135deg,#c9925a,#f1e4d4)"></div>
    <div class="icon"><svg width="30" height="24" viewBox="0 0 30 24" fill="#fff"><rect x="4" y="0" width="4" height="11"/><path d="M1 11h28v5a6 6 0 0 1-6 6H7a6 6 0 0 1-6-6z"/></svg></div>
    <div class="name">Bathrooms</div>
  </div>
  <div class="type" style="left:433px;top:123px">
    <div class="photo" role="img" aria-label="Kitchen interior photo" style="background:linear-gradient(135deg,#2e2e2e,#8a8a8a)"></div>
    <div class="icon"><svg width="32" height="24" viewBox="0 0 32 24" fill="#fff"><rect x="0" y="0" width="32" height="10"/><rect x="0" y="12" width="15" height="12"/><rect x="17" y="12" width="15" height="12"/></svg></div>
    <div class="name">Kitchen</div>
  </div>
  <div class="type" style="left:102px;top:335px">
    <div class="photo" role="img" aria-label="Dining room photo" style="background:linear-gradient(135deg,#5f7a4e,#c6b9a4)"></div>
    <div class="icon"><svg width="32" height="24" viewBox="0 0 32 24" fill="#fff"><rect x="4" y="8" width="24" height="4"/><rect x="6" y="12" width="3" height="12"/><rect x="23" y="12" width="3" height="12"/><rect x="0" y="2" width="3" height="22"/><rect x="29" y="2" width="3" height="22"/></svg></div>
    <div class="name">Dining Room</div>
  </div>
  <div class="type" style="left:268px;top:335px">
    <div class="photo" role="img" aria-label="Living room photo" style="background:linear-gradient(135deg,#3f5a72,#e2e4e6)"></div>
    <div class="icon"><svg width="30" height="24" viewBox="0 0 30 24" fill="#fff"><rect x="0" y="10" width="30" height="10" rx="2"/><rect x="4" y="4" width="22" height="7" rx="2"/><rect x="2" y="20" width="3" height="4"/><rect x="25" y="20" width="3" height="4"/></svg></div>
    <div class="name">Living Room</div>
  </div>
  <div class="type" style="left:433px;top:335px">
    <div class="photo" role="img" aria-label="Kids room photo" style="background:linear-gradient(135deg,#f1ece8,#cfc6c0)"></div>
    <div class="icon"><svg width="26" height="28" viewBox="0 0 26 28" fill="#fff"><rect x="0" y="6" width="10" height="22"/><rect x="12" y="14" width="14" height="14"/><circle cx="5" cy="3" r="3"/></svg></div>
    <div class="name">Kids Rooms</div>
  </div>

  <div class="abs pledge">Since its founding, Gwen Shines has been one of the most trusted names in the<br>industry. Hire us for this service and learn how we cater to the needs of each client,<br>ensuring the results you need and deserve.</div>
</section>

<section class="services">
  <div class="abs" role="img" aria-label="Photo of a smiling cleaner in a green apron and yellow gloves with arms crossed" style="left:0;top:14px;width:415px;height:535px;background:linear-gradient(180deg,#e9e2de,#d9cfc9 40%,#3f8a4e 75%,#2e7440)"></div>
  <div class="card" style="left:408px">
    <div class="photo" role="img" aria-label="Photo of cleaners wiping and mopping an office" style="background:linear-gradient(135deg,#d7cfbf,#3d7a4a 60%,#e8d36a)"></div>
    <div class="body">
      <h3>MOVE IN &amp; OUT CLEANING</h3>
      <h4>Expert Service</h4>
      <p>We have the experience and skills necessary to tackle just about every type of job that comes our way. With Gwen Shines, clients know exactly what to expect – professionalism, efficiency and exceptional results.</p>
    </div>
  </div>
  <div class="card" style="left:760px">
    <div class="photo" role="img" aria-label="Photo of a cleaner in yellow gloves scrubbing a white bathtub" style="background:linear-gradient(135deg,#e8ecef,#bfc8cf 55%,#e2cf6a)"></div>
    <div class="body">
      <h3>DEEP CLEANING</h3>
      <h4>Always Prepared</h4>
      <p>Gwen Shines is committed to getting the job done, especially when it comes to this service. You can count on us to be professional, timely, efficient and make sure you're satisfied every step of the way.</p>
    </div>
  </div>
</section>

<section class="intro">
  <div class="kicker script">Modern Bedroom</div>
  <h2>INTRODUCING GWEN SHINES</h2>
  <div class="tag">Exceptional Service</div>
  <div class="rule" style="left:112px;top:228px;width:976px;background:#e4e4e4"></div>
  <div class="rule" style="left:210px;top:231px;width:780px;background:#d8d8d8"></div>
</section>

<section class="about">
  <h2 class="script">About Us</h2>
  <h3>Reliable &amp; Honest</h3>
  <p>Our mission at Gwen's Shine is simple: to provide high-quality services for our valued clients. Our team goes above and beyond to cater to each project's specific needs. Through open communication and exceptional service, we hope you'll find what you're looking for with our House Cleaning Service. For more information or general inquiries, get in touch today.</p>
  <div class="abs photo" role="img" aria-label="Photo of two cleaners dusting and wiping furniture in a sunny room"></div>
</section>

<footer class="site-footer">
  <div class="col" style="left:113px">
    <h5>Site Map</h5>
    <ul><li>Home</li><li>About</li><li>Services</li><li>Contact Us</li></ul>
  </div>
  <div class="col" style="left:330px">
    <h5>Type of Services</h5>
    <ul><li>Bedroom Interior</li><li>Bathrooms</li><li>Kitchen</li><li>Dining room</li><li>Living room</li><li>Kids rooms</li></ul>
  </div>
  <div class="col" style="left:585px">
    <h5>Opening Hours</h5>
    <div class="hours">Contact By Text after 9am -10pm<br>Available Cleaning Time<br>Weekly Cleaning Plans<br>Mon - Fri:<br>9am - 5pm<br><b style="display:block;margin-top:13px">Saturday- Sunday: Please Contact</b></div>
  </div>
  <div class="col" style="left:871px">
    <h5>Get In Touch With Us</h5>
    <div class="contact-line"><svg width="16" height="11" viewBox="0 0 16 11"><rect width="16" height="11" fill="#ec1f27"/><path d="M0 0l8 6 8-6" stroke="#fff" stroke-width="1.3" fill="none"/></svg>hello@gwenshines.net</div>
    <div class="contact-line" style="margin-top:12px"><svg width="16" height="16" viewBox="0 0 24 24"><path fill="#ec1f27" d="M6.6 10.8a15 15 0 0 0 6.6 6.6l2.2-2.2a1 1 0 0 1 1-.25 11.4 11.4 0 0 0 3.6.57 1 1 0 0 1 1 1V20a1 1 0 0 1-1 1A17 17 0 0 1 3 4a1 1 0 0 1 1-1h3.5a1 1 0 0 1 1 1c0 1.25.2 2.45.57 3.6a1 1 0 0 1-.25 1z"/></svg>352-555-0148</div>
    <div class="social"><span aria-label="Social link"></span><span aria-label="Social link"></span><span aria-label="Social link"></span></div>
  </div>
</footer>

<div class="abs cta">
  <div class="name script">Gwen's Shine</div>
  <div class="call">Call Now:352-555-0148</div>
</div>

<div class="abs copyright" style="left:0;width:1200px">© 2019 Gwen Shines. All rights reserved.</div>

</body>
</html>
```